Lantern Bay Strong Bonds and Households Program-Youth

We need a flyer that invites high school students to our program. The students go through healthy relationship education, financial stability and workforce readiness.

We are in five locations, so we need a flyer that we can edit the text to update addresses, dates and any additional information based on our needs.

Attached are the two logo's we would like to use. I have also attached a previous flyer that we created to give you an idea of the text that is included.

In the past we have only promoted the healthy relationship component, but if you are able to incorporate finances (money) and job development (jobs), that would be great.

Must have
• Targets high school students
• Make the text available for us to edit
• Our topics is healthy relationship, money and jobs

```html
<!DOCTYPE html>
<html lang="en">
<head>
<meta charset="UTF-8">
<title>Lantern Bay Strong Bonds and Households – Youth Workshops</title>
<link rel="stylesheet" href="https://fonts.googleapis.com/css2?family=Roboto+Condensed:wght@400;700&family=Roboto+Slab:wght@400..900&family=Tinos&display=swap">
<style>
  :root {
    --navy: #0d2a52;
    --headline-blue: #0f3a66;
    --sky: #22b3e0;
    --sky-light: #bfeaf8;
    --orange: #e08a22;
    --white: #ffffff;
    --ink: #0a0a0a;
    --page: #e9eaec;
    --crowd-dark: #1b2230;
    --crowd-mid: #3a4658;
  }
  * { margin: 0; padding: 0; box-sizing: border-box; }
  html, body { width: 1200px; height: 1200px; overflow: hidden; background: var(--page); }
  .flyer {
    position: absolute; left: 150px; top: 20px;
    width: 900px; height: 1160px; overflow: hidden;
    background: radial-gradient(ellipse 620px 560px at 450px 600px, #ffffff 0%, #e8f8fd 30%, var(--sky-light) 55%, var(--sky) 100%);
    font-family: "Roboto Condensed", sans-serif;
  }
  .flyer-shapes { position: absolute; inset: 0; }
  .intro {
    position: absolute; top: 100px; left: 0; width: 900px; padding-left: 40px;
    text-align: center; font-weight: 700; font-size: 38px; color: var(--ink); letter-spacing: 0.3px;
    white-space: nowrap;
  }
  .topic-line {
    position: absolute; left: 235px; width: 500px; text-align: center;
    color: var(--headline-blue); white-space: nowrap;
  }
  .t-rel { top: 194px; font-weight: 700; font-size: 46px; line-height: 52px; }
  .t-edu { top: 238px; font-family: "Roboto Slab", serif; font-weight: 900; font-size: 40px; letter-spacing: 17px; line-height: 46px; padding-left: 17px; }
  .t-fin { top: 290px; font-family: "Tinos", serif; font-size: 48px; line-height: 56px; }
  .t-fin span { display: inline-block; transform: scaleX(.86); transform-origin: center; }
  .t-and { top: 352px; font-weight: 700; font-size: 32px; line-height: 36px; }
  .t-jobs { top: 392px; font-weight: 700; font-size: 36px; line-height: 44px; }
  .crowd {
    position: absolute; left: 142px; top: 452px; width: 622px; height: 272px;
    border-radius: 120px 120px 60px 60px;
    background: linear-gradient(180deg, var(--crowd-mid) 0%, var(--crowd-dark) 100%);
  }
  .schedule {
    position: absolute; left: 69px; top: 778px; color: var(--white);
    font-size: 20px; line-height: 26px; text-transform: uppercase;
  }
  .brace { position: absolute; left: 524px; top: 772px; }
  .location { position: absolute; left: 576px; top: 768px; color: var(--white); text-transform: uppercase; }
  .location h2 { font-weight: 400; font-size: 20px; line-height: 24px; }
  .location p { font-size: 14px; line-height: 17.5px; }
  .partners { position: absolute; left: 0; top: 879px; width: 900px; height: 145px; display: flex; align-items: center; }
  .partner-name {
    flex: 1; text-align: center; font-weight: 700; font-size: 22px; line-height: 28px; color: var(--navy);
    display: flex; align-items: center; justify-content: center; gap: 12px;
  }
  .partner-name .dot { width: 16px; height: 16px; border-radius: 50%; background: var(--orange); flex: none; }
  .contact { position: absolute; left: 0; top: 1030px; width: 900px; text-align: center; color: var(--white); }
  .contact h2 { font-weight: 400; font-size: 21px; line-height: 26px; }
  .contact .line { font-size: 17px; line-height: 22px; }
  .contact .line span { margin: 0 14px; }
  .funding { margin-top: 8px; font-size: 10px; line-height: 14px; color: var(--orange); }
</style>
</head>
<body>
<main class="flyer">
  <svg class="flyer-shapes" width="900" height="1160" viewBox="0 0 900 1160" aria-hidden="true">
    <path d="M0 653 Q380 790 900 621 L900 879 L0 879 Z" fill="var(--orange)"/>
    <path d="M0 653 Q390 800 900 674 L900 879 L0 879 Z" fill="var(--navy)"/>
    <rect x="0" y="879" width="900" height="145" fill="var(--white)"/>
    <rect x="0" y="1024" width="900" height="136" fill="var(--navy)"/>
  </svg>

  <h1 class="intro">WORKSHOPS FOR HIGH SCHOOL STUDENTS ON</h1>

  <div class="topic-line t-rel">HEALTHY RELATIONSHIP</div>
  <div class="topic-line t-edu">EDUCATION,</div>
  <div class="topic-line t-fin"><span>FINANCIAL STABILITY</span></div>
  <div class="topic-line t-and">AND</div>
  <div class="topic-line t-jobs">WORKFORCE READINESS (JOBS)</div>

  <div class="crowd" role="img" aria-label="Silhouettes of a group of teenagers jumping with arms raised"></div>

  <p class="schedule">Workshops will be held every Wednesday<br>for 10 weeks starting January 10th.<br>From 5:30PM—7:30PM</p>

  <svg class="brace" width="34" height="100" viewBox="0 0 34 100" aria-hidden="true">
    <path d="M4 3 Q18 3 18 20 L18 38 Q18 50 30 50 Q18 50 18 62 L18 80 Q18 97 4 97" fill="none" stroke="var(--white)" stroke-width="2"/>
  </svg>

  <div class="location">
    <h2>LOCATION:</h2>
    <p>Cove Family Resource Center<br>1840 Tidewater Lane<br>Lantern Bay, CA 90410<br>(555) 489-0142</p>
  </div>

  <div class="partners">
    <div class="partner-name"><span class="dot"></span>Lantern Bay Strong Bonds<br>and Households</div>
    <div class="partner-name"><span class="dot"></span>Harborline Community<br>Partnership</div>
  </div>

  <div class="contact">
    <h2>FOR MORE INFORMATION CALL:</h2>
    <p class="line">Marisol Dern, LB-SBH Program Coordinator<span>|</span>Phone: 555-406-0128<span>|</span>E-mail: mdern@harborline.org</p>
    <p class="funding">“Funding for this project was provided by the Regional Office of Family and Youth Services, Grant: #47LB2261.<br>These services are available to all eligible persons, regardless of race, gender, age, disability, or religion.”</p>
  </div>
</main>
</body>
</html>
```